Professional law firm looking for new professional and eye-catching business card design

Law firm in need of new business card design using existing firm logo and firm colors on thick card stock. Firm colors are navy blue, cyan blue, and gray. Please use firm's logo either on the back of the card or on the front and back. I am looking for something eye-catching and resonating but also professional.

Target Market(s)

Law firm growth by attracting clients with professional, creative, and attractive business cards.

Industry/Entity Type

Legal/Law Firm

Contact Information for Business Card

Name: Derek T. Halloway, Esq., Address: 517 E. Quintley Blvd., P.O. Box 641, Larkmoor, NV 89910, Phone numbers: (555) 555-0187 Office, (555) 555-0142 Fax, email address: DerekH@hqlegalfx.com, website: www.HQLegalFX.com

Font styles to use
Other font styles liked:
• Font as close as possible to matching law firm logo.

Requirements
Must have
• Must have business card details and law firm logo with law firm colors.

```html
<!DOCTYPE html>
<html lang="en">
<head>
<meta charset="utf-8">
<title>HQ Legal – Business Card</title>
<link href="https://fonts.googleapis.com/css2?family=Cinzel:wght@500;700&family=Figtree:wght@400&display=swap" rel="stylesheet">
<style>
  :root {
    --stage: #23272f;
    --navy: #181e2a;
    --cyan: #00aeef;
    --cyan-deep: #0aa4e0;
    --gray: #a9a8ad;
    --silver: #b9b9bd;
    --ink: #1d2430;
  }
  * { box-sizing: border-box; margin: 0; padding: 0; }
  html, body {
    width: 1200px; height: 1000px; overflow: hidden;
    background: var(--stage);
  }
  .card {
    position: absolute; top: 94px; width: 423px; height: 760px;
    background: var(--navy); overflow: hidden;
  }
  .card--back { left: 128px; }
  .card--front { left: 604px; }

  .justice-figure {
    position: absolute;
    background: linear-gradient(180deg, #c4c4c8 0%, #9d9da2 100%);
    border-radius: 40px 40px 14px 14px;
    opacity: .85;
  }
  .card--back .justice-figure { left: 72px; top: 186px; width: 80px; height: 282px; }
  .card--front .justice-figure { left: 76px; top: 82px; width: 80px; height: 268px; }

  .firm-name {
    position: absolute;
    font-family: "Cinzel", serif; font-weight: 700;
    color: var(--cyan-deep); font-size: 38px; letter-spacing: 3px;
    white-space: nowrap; line-height: 1;
  }
  .card--back .firm-name { left: 162px; top: 340px; }
  .card--front .firm-name { left: 166px; top: 230px; }

  .back-stripe { position: absolute; left: 0; top: 660px; width: 100%; height: 11px; background: var(--cyan); }
  .back-band {
    position: absolute; left: 0; top: 671px; width: 100%; height: 89px;
    background: var(--gray);
    display: flex; align-items: center; justify-content: center;
  }
  .website {
    font-family: "Cinzel", serif; font-weight: 700; font-size: 22px;
    color: var(--ink); letter-spacing: .5px;
  }

  .name-band {
    position: absolute; left: 0; top: 438px; width: 100%; height: 96px;
    background: var(--cyan);
    display: flex; align-items: center; justify-content: center;
  }
  .attorney-name {
    font-family: "Cinzel", serif; font-weight: 700; font-size: 24px;
    color: var(--ink); letter-spacing: .5px; white-space: nowrap;
  }
  .contact-list { position: absolute; left: 0; top: 536px; width: 100%; list-style: none; }
  .contact-row {
    display: flex; height: 33px; margin-bottom: 1px;
    background: var(--gray);
  }
  .contact-row--tall { height: 44px; }
  .contact-icon {
    margin-left: 34px; width: 81px; background: var(--navy);
    display: flex; align-items: center; justify-content: center;
  }
  .contact-icon svg { width: 22px; height: 22px; }
  .contact-text {
    padding-left: 19px; display: flex; align-items: center;
    font-family: "Figtree", sans-serif; font-size: 17px; color: #2a2f38;
    line-height: 1.05;
  }
  .front-foot { position: absolute; left: 0; top: 714px; width: 100%; height: 46px; background: var(--cyan); }
</style>
</head>
<body>

<section class="card card--back" aria-label="Card back">
  <div class="justice-figure" role="img" aria-label="Illustration of Lady Justice holding scales and a sword"></div>
  <div class="firm-name">HQ LEGAL</div>
  <div class="back-stripe"></div>
  <div class="back-band"><span class="website">www.HQLegalFX.com</span></div>
</section>

<section class="card card--front" aria-label="Card front">
  <div class="justice-figure" role="img" aria-label="Illustration of Lady Justice holding scales and a sword"></div>
  <div class="firm-name">HQ LEGAL</div>

  <div class="name-band"><h1 class="attorney-name">Derek T. Halloway, Esq.</h1></div>

  <ul class="contact-list">
    <li class="contact-row">
      <span class="contact-icon">
        <svg viewBox="0 0 24 24" fill="none" stroke="#00aeef" stroke-width="2"><rect x="2" y="5" width="20" height="14"/><path d="M2 5l10 8 10-8"/></svg>
      </span>
      <span class="contact-text">DerekH@hqlegalfx.com</span>
    </li>
    <li class="contact-row">
      <span class="contact-icon">
        <svg viewBox="0 0 24 24" fill="none" stroke="#00aeef" stroke-width="2"><path d="M5 3h4l2 5-3 2a11 11 0 0 0 6 6l2-3 5 2v4a2 2 0 0 1-2 2A18 18 0 0 1 3 5a2 2 0 0 1 2-2z"/></svg>
      </span>
      <span class="contact-text">(555) 555-0187</span>
    </li>
    <li class="contact-row">
      <span class="contact-icon">
        <svg viewBox="0 0 24 24" fill="#00aeef"><rect x="2" y="8" width="5" height="14"/><rect x="8" y="3" width="14" height="19"/><rect x="10" y="5" width="10" height="5" fill="#181e2a"/><rect x="10" y="13" width="2" height="2" fill="#181e2a"/><rect x="14" y="13" width="2" height="2" fill="#181e2a"/><rect x="18" y="13" width="2" height="2" fill="#181e2a"/><rect x="10" y="17" width="2" height="2" fill="#181e2a"/><rect x="14" y="17" width="2" height="2" fill="#181e2a"/><rect x="18" y="17" width="2" height="2" fill="#181e2a"/></svg>
      </span>
      <span class="contact-text">(555) 555-0142</span>
    </li>
    <li class="contact-row">
      <span class="contact-icon">
        <svg viewBox="0 0 24 24" fill="none" stroke="#00aeef" stroke-width="2"><path d="M12 21s-6-6-6-11a6 6 0 0 1 12 0c0 5-6 11-6 11z"/><circle cx="12" cy="10" r="2"/><path d="M4 21h16"/></svg>
      </span>
      <span class="contact-text">517 E. Quintley Blvd</span>
    </li>
    <li class="contact-row contact-row--tall">
      <span class="contact-icon">
        <svg viewBox="0 0 24 24" fill="#00aeef"><path d="M3 10a5 5 0 0 1 10 0v8H3z"/><path d="M9 5h9a4 4 0 0 1 4 4v9H14v-8a5 5 0 0 0-5-5z"/><rect x="11" y="18" width="3" height="5"/><rect x="6" y="1" width="2" height="7"/><rect x="8" y="1" width="5" height="3"/></svg>
      </span>
      <span class="contact-text">P.O. Box 641, Larkmoor,<br>NV 89910</span>
    </li>
  </ul>

  <div class="front-foot"></div>
</section>

</body>
</html>
```